Business Cards Needed For Veterinary Business

Looking for a business card design for a veterinary blood bank. We would like it to be clean and professional on appearance but still warm and inviting. We would like to utilize our logo and similar coloring. We will use our phone number, email, website, employee name, employee title.

We do not want a bunch of animated animal photos but do not need the style to be as clinical as a laboratory or human medical procedure office.

We are looking for some creative ideas to choose from so that we can generate a standout professional business card for our management team to utilize.

Target Market(s)

professionals

Industry/Entity Type

veterinary

Contact Information for Business Card

employee name, employee title, phone number, website URL, email

Font styles to use
Sans Serif

Colors
0054AA
0677BA
7BADD7
CADEEF
E8F1F8
EB3D1F
EC4F4E
F09395
F8D3D4
FCEDEE

Requirements
Nice to have
• creative design
Should not have
• animated photos

```html
<!DOCTYPE html>
<html lang="en">
<head>
<meta charset="utf-8">
<title>Brightwater Vet Blood Bank – Business Card</title>
<link href="https://fonts.googleapis.com/css2?family=Arimo:wght@700&family=Lato:wght@400&display=swap" rel="stylesheet">
<style>
  :root {
    --brand-red: #ec1c24;
    --brand-blue: #0f57a8;
    --ink-white: #ffffff;
    --card-white: #ffffff;
    --page-bg: #f2f2f2;
    --faint-red: #fcedee;
  }
  * { margin: 0; padding: 0; box-sizing: border-box; }
  html, body {
    width: 1000px; height: 1200px; overflow: hidden;
    background: var(--page-bg);
  }
  .canvas { position: relative; width: 1000px; height: 1200px; }

  .card {
    position: absolute; left: 83px; width: 829px; height: 473px;
    background: var(--card-white); overflow: hidden;
  }
  .card--front { top: 81px; }
  .card--back { top: 639px; }

  /* Brand lockup */
  .brand {
    position: absolute; display: flex; align-items: center; gap: 16px;
    font-family: "Arimo", Arial, sans-serif; font-weight: 700;
    color: var(--brand-red); font-size: 34px; white-space: nowrap;
  }
  .brand__dot {
    width: 84px; height: 84px; border-radius: 50%;
    background: var(--brand-red); flex: none;
  }
  .card--front .brand { left: 50%; top: 73px; transform: translateX(-50%); }
  .card--back .brand { left: 50%; top: 194px; transform: translateX(-50%); }

  /* Front: bands */
  .front__blue {
    position: absolute; left: 0; top: 268px; width: 100%; height: 205px;
    background: var(--brand-blue);
  }
  .front__redline {
    position: absolute; left: 300px; top: 259px; right: 0; height: 9px;
    background: var(--brand-red);
  }
  .front__banner { position: absolute; left: 0; top: 232px; width: 330px; height: 73px; }

  .person { position: absolute; left: 36px; top: 232px; color: var(--ink-white);
    font-family: "Arimo", Arial, sans-serif; font-weight: 700; }
  .person__name { font-size: 44px; line-height: 1; margin-top: 7px; letter-spacing: 0.2px; }
  .person__title { font-size: 17px; line-height: 1; margin-top: 5px; }

  .contacts {
    position: absolute; left: 38px; top: 351px; list-style: none;
    font-family: "Lato", Arial, sans-serif; font-size: 21px; color: var(--ink-white);
  }
  .contacts li { display: flex; align-items: center; height: 28.5px; }
  .contacts svg { width: 20px; height: 20px; margin-right: 15px; fill: var(--ink-white); flex: none; }

  .address {
    position: absolute; left: 545px; top: 385px;
    font-family: "Lato", Arial, sans-serif; font-size: 22px; line-height: 26px;
    color: var(--ink-white); font-style: normal;
  }

  /* Back */
  .back__ghost {
    position: absolute; left: 650px; top: 90px; width: 360px; height: 360px;
    border-radius: 50%; background: var(--faint-red);
  }
  .back__stripe-red { position: absolute; left: 0; top: 433px; width: 100%; height: 16px; background: var(--brand-red); }
  .back__stripe-blue { position: absolute; left: 0; top: 460px; width: 100%; height: 13px; background: var(--brand-blue); }
</style>
</head>
<body>
<main class="canvas">

  <section class="card card--front">
    <div class="brand"><span class="brand__dot"></span><span>Brightwater Vet Blood Bank</span></div>

    <div class="front__redline"></div>
    <div class="front__blue"></div>
    <svg class="front__banner" viewBox="0 0 330 73" preserveAspectRatio="none">
      <polygon points="0,0 326,0 282,73 0,73" fill="var(--brand-red)"/>
    </svg>

    <div class="person">
      <div class="person__name">Calder Moss</div>
      <div class="person__title">DIRECTOR</div>
    </div>

    <ul class="contacts">
      <li>
        <svg viewBox="0 0 24 24"><path d="M6.6 10.8a15.1 15.1 0 0 0 6.6 6.6l2.2-2.2c.3-.3.7-.4 1-.2 1.1.4 2.3.6 3.6.6.6 0 1 .4 1 1V20c0 .6-.4 1-1 1C10.6 21 3 13.4 3 4c0-.6.4-1 1-1h3.5c.6 0 1 .4 1 1 0 1.3.2 2.5.6 3.6.1.3 0 .7-.2 1z"/></svg>
        555-014-2290
      </li>
      <li>
        <svg viewBox="0 0 24 24"><path d="M2 5h20v14H2z M3.5 6.5 12 13l8.5-6.5" fill="none" stroke="#fff" stroke-width="1.8"/></svg>
        calder@maildesk.com
      </li>
      <li>
        <svg viewBox="0 0 24 24"><circle cx="12" cy="12" r="9.5" fill="none" stroke="#fff" stroke-width="2"/><path d="M2.5 12h19M12 2.5c3 3 3 16 0 19M12 2.5c-3 3-3 16 0 19" fill="none" stroke="#fff" stroke-width="1.5"/></svg>
        www.calmoss.com
      </li>
    </ul>

    <address class="address">2715 Ferncliff Dr #318<br>Lindale, MD 20945</address>
  </section>

  <section class="card card--back">
    <div class="back__ghost"></div>
    <div class="brand"><span class="brand__dot"></span><span>Brightwater Vet Blood Bank</span></div>
    <div class="back__stripe-red"></div>
    <div class="back__stripe-blue"></div>
  </section>

</main>
</body>
</html>
```